Want a package created for a new protein bar

We would like a new package created for a new protein bar project The name of the bar will be VOLMBite a real food protein bar, we would like a ‘window’ on the package of bar like Brave Meadow bar below in images.

VOLMBite
‘Super Food Bar’
14g of Whey Protein
The package film size is the following 12cm width x 15cm Length,
Flavor Peanut Chocolate Chip, additional information will be attached shortly like nutrition facts,

Target Market(s)

fitness market, bodybuilders, athletes, everyday people

Industry/Entity Type

Health Product

Logo Text

VOLMBite

Font styles to use
Serif
Sans Serif
Decorative

Requirements
Must have
• Package window

```html
<!DOCTYPE html>
<html lang="en">
<head>
<meta charset="utf-8">
<title>VOLMBite – Peanut Chocolate Chip Wrapper</title>
<link rel="stylesheet" href="https://fonts.googleapis.com/css2?family=Archivo:wght@400;800&display=swap">
<style>
  :root {
    --backdrop: #e9e9e9;
    --wrapper-dark: #241610;
    --wrapper-brown: #3e2a1f;
    --crimp-brown: #4a3327;
    --crimp-line: #2a1a12;
    --flavor-gold: #e6c27f;
    --crimp-gold: #eac784;
    --crimp-gold-line: #c9a05a;
    --logo-silver: #d2d0cd;
    --tagline: #c9c6c2;
    --flavor-text: #ffffff;
    --protein-text: #111111;
    --window-light: #e9b24a;
    --window-dark: #b9822f;
  }
  html, body {
    margin: 0;
    width: 1200px;
    height: 686px;
    overflow: hidden;
    background: var(--backdrop);
  }
  .package {
    display: block;
    width: 1200px;
    height: 686px;
  }
  .brand-name {
    font-family: "Archivo", Arial, sans-serif;
    font-weight: 800;
    font-size: 72px;
    fill: var(--logo-silver);
  }
  .tagline {
    font-family: "Archivo", Arial, sans-serif;
    font-weight: 400;
    font-size: 30px;
    fill: var(--tagline);
  }
  .flavor-name {
    font-family: "Archivo", Arial, sans-serif;
    font-weight: 800;
    font-size: 33px;
    fill: var(--flavor-text);
  }
  .protein-claim {
    font-family: "Archivo", Arial, sans-serif;
    font-weight: 800;
    font-size: 17px;
    fill: var(--protein-text);
  }
</style>
</head>
<body>
<svg class="package" viewBox="0 0 1200 686" xmlns="http://www.w3.org/2000/svg">
  <defs>
    <linearGradient id="wrapper-shade" x1="0" y1="0" x2="0" y2="1">
      <stop offset="0" stop-color="var(--wrapper-brown)"/>
      <stop offset="0.45" stop-color="var(--wrapper-dark)"/>
      <stop offset="1" stop-color="var(--wrapper-brown)"/>
    </linearGradient>
    <linearGradient id="window-tone" x1="0" y1="0" x2="1" y2="1">
      <stop offset="0" stop-color="var(--window-dark)"/>
      <stop offset="0.5" stop-color="var(--window-light)"/>
      <stop offset="1" stop-color="var(--window-dark)"/>
    </linearGradient>
    <pattern id="crimp-dark" width="6" height="10" patternUnits="userSpaceOnUse">
      <rect width="6" height="10" fill="var(--crimp-brown)"/>
      <rect width="2" height="10" fill="var(--crimp-line)"/>
    </pattern>
    <pattern id="crimp-light" width="6" height="10" patternUnits="userSpaceOnUse">
      <rect width="6" height="10" fill="var(--crimp-gold)"/>
      <rect width="2" height="10" fill="var(--crimp-gold-line)"/>
    </pattern>
  </defs>

  <!-- left end seal -->
  <rect class="seal seal-left" x="127" y="172" width="66" height="348" fill="url(#crimp-dark)"/>

  <!-- main wrapper body -->
  <rect class="wrapper-body" x="193" y="205" width="670" height="276" fill="url(#wrapper-shade)"/>

  <!-- product window -->
  <polygon class="product-window" role="img" aria-label="Window showing the peanut chocolate chip bar inside"
           points="660,205 863,205 863,481 573,481" fill="url(#window-tone)"/>

  <!-- flavour panel -->
  <rect class="flavor-panel" x="863" y="205" width="143" height="276" fill="var(--flavor-gold)"/>

  <!-- right end seal -->
  <rect class="seal seal-right" x="1006" y="172" width="67" height="348" fill="url(#crimp-light)"/>

  <!-- brand block -->
  <text class="brand-name" x="264" y="340">VOLMBite</text>
  <text class="tagline" x="304" y="385">Super Food Bar</text>

  <!-- flavour and claim, set vertically -->
  <g class="flavor-block" transform="translate(0 0)">
    <text class="flavor-name" transform="translate(898 420) rotate(-90)">Peanut</text>
    <text class="flavor-name" transform="translate(928 444) rotate(-90)">Chocolate</text>
    <text class="flavor-name" transform="translate(958 398) rotate(-90)">Chip</text>
    <text class="protein-claim" transform="translate(985 448) rotate(-90)">14g of Whey Protein</text>
  </g>
</svg>
</body>
</html>
```